Business Card Design

I need a business card design for a new company based in Australind, Western Australia. The business is for puppet shows at children's parties, fetes, custom puppet builds, etc.Attached is a picture of Ray Pellow in silhouette. I was thinking a design of a puppeteer at the top of some stairs talking to a puppet in silhouette but open to suggestions. (Lantern Loft is named as I do all my puppet builds in the top room of my house (at the Lantern Loft).

Industry/Entity Type

Business

Contact Information for Business Card

Lantern Loft Marionettes, Dale Voss, Puppeteer / Puppet Builder, phone - 0438562703, Puppet shows / Custom Puppet Builds, Working With Children

Requirements
Must have
• Name and Logo on one side. Second side to have business card details.

```html
<!DOCTYPE html>
<html lang="en">
<head>
<meta charset="utf-8">
<title>Lantern Loft Marionettes – Business Card</title>
<link rel="stylesheet" href="https://fonts.googleapis.com/css2?family=Open+Sans:wght@400;600&display=swap">
<style>
  :root {
    --page-bg: #ecebe8;
    --band-top: #5a5a5a;
    --band-bottom: #3b3b3b;
    --card-white: #ffffff;
    --ink-dark: #151515;
    --ink-light: #f4f4f4;
    --photo-light: #cdd6cc;
    --photo-mid: #6f776c;
    --photo-dark: #161913;
  }
  * { box-sizing: border-box; margin: 0; padding: 0; }
  html, body {
    width: 1200px; height: 800px; overflow: hidden;
    background: var(--page-bg);
    font-family: "Open Sans", "Segoe UI", sans-serif;
  }
  .card {
    position: absolute; left: 100px; top: 114px;
    width: 1000px; height: 572px;
    background: var(--card-white);
    box-shadow: 0 10px 30px rgba(0,0,0,0.18);
    overflow: hidden;
  }
  .card__header {
    position: absolute; left: 0; top: 0; width: 100%; height: 110px;
    background: linear-gradient(180deg, var(--band-top), #4a4a4a);
    display: flex; align-items: center; justify-content: flex-end;
    padding-right: 48px;
  }
  .brand-name {
    color: var(--ink-light); font-size: 46px; font-weight: 600;
    letter-spacing: 4px;
  }
  .card__photo {
    position: absolute; left: 0; top: 110px; width: 470px; height: 320px;
    background:
      linear-gradient(90deg, var(--photo-light) 0%, var(--photo-mid) 45%, var(--photo-dark) 75%, #2c2a22 100%);
  }
  .card__details {
    position: absolute; right: 48px; top: 210px;
    text-align: right; color: var(--ink-dark);
  }
  .role { font-size: 28px; letter-spacing: 2px; }
  .person-name { font-size: 48px; letter-spacing: 3px; line-height: 1.1; margin-top: 2px; }
  .phone { font-size: 28px; font-weight: 600; letter-spacing: 4px; margin-top: 6px; }
  .card__footer {
    position: absolute; left: 0; bottom: 0; width: 100%; height: 142px;
    background: linear-gradient(180deg, #474747, var(--band-bottom));
    color: var(--ink-light);
    padding: 28px 48px 0 40px;
    font-size: 30px; letter-spacing: 3px;
  }
  .services-line { display: flex; align-items: center; gap: 22px; }
  .divider { width: 5px; height: 34px; background: var(--ink-light); }
  .services-line--second { justify-content: flex-end; margin-top: 8px; }
</style>
</head>
<body>
  <div class="card">
    <header class="card__header">
      <span class="brand-name">Lantern Loft Marionettes</span>
    </header>
    <div class="card__photo" role="img" aria-label="Photo of a puppeteer in silhouette holding a puppet up in front of a bright window"></div>
    <div class="card__details">
      <p class="role">Puppeteer / Puppet Builder</p>
      <p class="person-name">Dale Voss</p>
      <p class="phone">0438562703</p>
    </div>
    <footer class="card__footer">
      <div class="services-line">
        <span class="id-number">3915286</span>
        <span class="divider"></span>
        <span>Puppet shows / Custom Puppet Builds,</span>
      </div>
      <div class="services-line services-line--second">
        <span>Working With Children</span>
      </div>
    </footer>
  </div>
</body>
</html>
```